Need Business Card ASAP

We need a business card design for a meeting coming up in a few days. The company name is Halvorne Building and Construction and the logo is attached. Something clean, cool, and contemporary that we can get to a printer right away. Attached is the business card for Murrow Energy, an affiliated company, which we like. Instead of the hawk on the back, you could use the attached "D". We'll also be needing matching letterhead in the near future, so ideas for that are welcome.

```html
<!DOCTYPE html>
<html lang="en">
<head>
<meta charset="utf-8">
<title>Halvorne Building and Construction – Business Card</title>
<link rel="stylesheet" href="https://fonts.googleapis.com/css2?family=Source+Sans+3:wght@400;600;700&family=Libre+Caslon+Text:wght@400&display=swap">
<style>
  :root {
    --khaki: #c4bb84;
    --khaki-text: #c2b27b;
    --ink: #231f20;
    --text: #2b2b2b;
    --paper: #ffffff;
    --stage: #dcd7ce;
    --rule: #d8d8d8;
  }
  * { margin: 0; padding: 0; box-sizing: border-box; }
  html, body { width: 1034px; height: 1200px; overflow: hidden; }
  body {
    position: relative;
    background: var(--stage);
    font-family: "Source Sans 3", "Helvetica Neue", Arial, sans-serif;
    color: var(--text);
  }

  /* Front card */
  .card-front { position: absolute; left: 61px; top: 71px; width: 885px; height: 504px; }
  .frame-quad { position: absolute; }
  .frame-quad.top-left     { left: 0; top: 0; width: 420px; height: 242px; background: var(--khaki); }
  .frame-quad.top-right    { left: 437px; top: 0; width: 448px; height: 242px; background: var(--ink); }
  .frame-quad.bottom-left  { left: 0; top: 258px; width: 420px; height: 246px; background: var(--ink); }
  .frame-quad.bottom-right { left: 437px; top: 258px; width: 448px; height: 246px; background: var(--khaki); }
  .frame-gap-v { position: absolute; left: 420px; top: 0; width: 17px; height: 504px; background: var(--paper); }
  .frame-gap-h { position: absolute; left: 0; top: 242px; width: 885px; height: 16px; background: var(--paper); }

  .card-face {
    position: absolute; left: 20px; top: 17px; width: 849px; height: 470px;
    background: var(--paper);
  }

  .brand-block { position: absolute; left: 139px; top: 67px; width: 186px; text-align: center; }
  .brand-square { width: 186px; height: 160px; background: var(--khaki); }
  .brand-name {
    margin-top: 12px;
    font-family: "Libre Caslon Text", Georgia, serif;
    font-size: 34px; font-weight: 400; color: var(--ink);
  }

  .divider {
    position: absolute; left: 358px; top: 64px; width: 2px; height: 245px;
    background: linear-gradient(to bottom, #f2f2f2, #c9c9c9, #f2f2f2);
  }

  .person { position: absolute; left: 384px; top: 68px; }
  .person-name { font-size: 33px; font-weight: 700; color: var(--khaki-text); line-height: 1; }
  .person-title { margin-top: 9px; font-size: 21px; font-weight: 700; color: var(--text); }

  .contact-list { position: absolute; left: 380px; top: 166px; list-style: none; }
  .contact-list li {
    display: flex; align-items: center; height: 41px;
    font-size: 25px; color: var(--text);
  }
  .contact-list svg { width: 20px; height: 20px; margin-right: 12px; fill: var(--text); }

  .footer-rule {
    position: absolute; left: 40px; top: 360px; width: 770px; height: 2px;
    background: linear-gradient(to right, transparent, var(--rule), transparent);
  }
  .company { position: absolute; left: 0; top: 385px; width: 100%; text-align: center; }
  .company-name { font-size: 29px; font-weight: 600; color: var(--khaki-text); line-height: 1.1; }
  .company-address { margin-top: 6px; font-size: 20px; color: var(--text); }

  /* Back card */
  .card-back {
    position: absolute; left: 61px; top: 614px; width: 885px; height: 507px;
    background: var(--khaki);
    display: flex; align-items: center; justify-content: center;
  }
  .back-name {
    font-family: "Libre Caslon Text", Georgia, serif;
    font-size: 110px; font-weight: 400; color: var(--paper);
  }
</style>
</head>
<body>

<section class="card-front" aria-label="Business card front">
  <div class="frame-quad top-left"></div>
  <div class="frame-quad top-right"></div>
  <div class="frame-quad bottom-left"></div>
  <div class="frame-quad bottom-right"></div>
  <div class="frame-gap-v"></div>
  <div class="frame-gap-h"></div>

  <div class="card-face">
    <div class="brand-block">
      <div class="brand-square"></div>
      <div class="brand-name">Halvorne</div>
    </div>

    <div class="divider"></div>

    <div class="person">
      <div class="person-name">Your Name</div>
      <div class="person-title">Title</div>
    </div>

    <ul class="contact-list">
      <li>
        <svg viewBox="0 0 20 20" aria-hidden="true"><path d="M5 2c1 0 1.5.4 2 1.5l1 2.5c.3.8 0 1.4-.6 1.9l-1 .8c.9 2 2.4 3.5 4.4 4.4l.8-1c.5-.6 1.1-.9 1.9-.6l2.5 1c1.1.5 1.5 1 1.5 2 0 1.6-1.6 3.5-3.5 3.5C7.5 18 2 12.5 2 5.5 2 3.6 3.4 2 5 2z"/></svg>
        (123) 456-7890
      </li>
      <li>
        <svg viewBox="0 0 20 20" aria-hidden="true"><path d="M6 1h8a1 1 0 0 1 1 1v16a1 1 0 0 1-1 1H6a1 1 0 0 1-1-1V2a1 1 0 0 1 1-1zm1 3v10h6V4H7zm3 11.5a1 1 0 1 0 0 2 1 1 0 0 0 0-2z"/></svg>
        (123) 456-7890
      </li>
      <li>
        <svg viewBox="0 0 20 20" aria-hidden="true"><path d="M2 8l8-5 8 5v9H2V8zm2 1.2V15h12V9.2l-6 3.6-6-3.6z"/></svg>
        yourname@halvorne.com
      </li>
      <li>
        <svg viewBox="0 0 20 20" aria-hidden="true"><path d="M10 1.5a8.5 8.5 0 1 0 0 17 8.5 8.5 0 0 0 0-17zm-6.3 7.5h2.8c.1-1.8.5-3.4 1.1-4.6A6.6 6.6 0 0 0 3.7 9zm0 2a6.6 6.6 0 0 0 3.9 4.6c-.6-1.2-1-2.8-1.1-4.6H3.7zm4.8 0c.2 2.6 1 4.4 1.5 4.9.5-.5 1.3-2.3 1.5-4.9h-3zm3 -2c-.2-2.6-1-4.4-1.5-4.9-.5.5-1.3 2.3-1.5 4.9h3zm2 2c-.1 1.8-.5 3.4-1.1 4.6a6.6 6.6 0 0 0 3.9-4.6h-2.8zm2.8-2a6.6 6.6 0 0 0-3.9-4.6c.6 1.2 1 2.8 1.1 4.6h2.8z"/></svg>
        www.halvorne.com
      </li>
    </ul>

    <div class="footer-rule"></div>

    <div class="company">
      <div class="company-name">Halvorne Building and Construction</div>
      <div class="company-address">00, Complex Name, Street, City 00000</div>
    </div>
  </div>
</section>

<section class="card-back" aria-label="Business card back">
  <div class="back-name">Halvorne</div>
</section>

</body>
</html>
```